International Sustainable Cities NGO needs PPT Design

We need a PPT design for a presentation upcoming at a leading university on the East coast. The design needs to be clean and simple, professional and room for photos and maps. It's a presentation about citizen mapping and data collection for city planning/decision making.

University

```html
<!DOCTYPE html>
<html lang="en">
<head>
<meta charset="utf-8">
<title>City Data Slide</title>
<link rel="stylesheet" href="https://fonts.googleapis.com/css2?family=Arimo:ital,wght@0,400;0,700;1,400&display=swap">
<style>
  :root {
    --navy: #13294b;
    --navy-deep: #0c1d38;
    --navy-light: #1f3b63;
    --teal: #2bb5c2;
    --gold: #f5c018;
    --rule-grey: #d3d3d3;
    --caption-grey: #8a8a8a;
    --white: #ffffff;
  }
  * { box-sizing: border-box; margin: 0; padding: 0; }
  html, body { width: 1200px; height: 900px; overflow: hidden; background: var(--white); }
  body { font-family: "Arimo", Arial, sans-serif; }
  .slide { position: relative; width: 1200px; height: 900px; background: var(--white); overflow: hidden; }

  .header-band {
    position: absolute; left: 0; top: 0; width: 1200px; height: 138px;
    background: linear-gradient(180deg, var(--navy-light) 0%, var(--navy) 55%, var(--navy-deep) 100%);
  }
  .header-shade {
    position: absolute; left: 0; top: 138px; width: 1200px; height: 26px;
    background: linear-gradient(180deg, #b9b9b9 0%, rgba(255,255,255,0) 100%);
  }
  .slide-title {
    position: absolute; left: 20px; top: 44px;
    color: var(--white); font-size: 49px; font-weight: 400; letter-spacing: 0.2px;
  }

  .download-icon { position: absolute; left: 554px; top: 160px; width: 92px; height: 92px; }

  .metric-label {
    position: absolute; left: 0; width: 1200px; top: 268px; text-align: center;
    color: var(--teal); font-size: 51px; font-weight: 400;
  }
  .metric-value {
    position: absolute; left: 0; width: 1200px; top: 332px; text-align: center;
    color: var(--teal); font-size: 57px; font-weight: 700;
  }
  .thin-rule { position: absolute; left: 323px; top: 418px; width: 555px; height: 1px; background: var(--rule-grey); }
  .location-note {
    position: absolute; left: 0; width: 1200px; top: 436px; text-align: center;
    color: var(--navy); font-size: 27px; font-style: italic;
  }
  .gold-rule { position: absolute; left: 88px; top: 486px; width: 1023px; height: 5px; background: var(--gold); }

  .targets-box {
    position: absolute; left: 22px; top: 530px; width: 1156px; height: 252px;
    border: 5px solid var(--teal); border-radius: 18px;
  }
  .divider-slash { position: absolute; left: 550px; top: 550px; width: 140px; height: 210px; }

  .target { position: absolute; top: 575px; width: 360px; text-align: center; }
  .target--left { left: 98px; }
  .target--right { left: 728px; }
  .target-figure {
    color: var(--navy); font-size: 108px; font-weight: 700; line-height: 1; letter-spacing: -2px;
  }
  .target-figure sup { font-size: 50px; vertical-align: 48px; margin-left: 4px; letter-spacing: 0; }
  .target-name { color: var(--teal); font-size: 45px; font-weight: 700; margin-top: -2px; line-height: 1.1; }
  .target-caption { color: var(--caption-grey); font-size: 23px; margin-top: 4px; word-spacing: 4px; }

  .footer-shade {
    position: absolute; left: 0; top: 812px; width: 1200px; height: 28px;
    background: linear-gradient(0deg, #b9b9b9 0%, rgba(255,255,255,0) 100%);
  }
  .footer-band {
    position: absolute; left: 0; top: 840px; width: 1200px; height: 60px;
    background: linear-gradient(180deg, var(--navy-light) 0%, var(--navy-deep) 100%);
  }
  .page-number { position: absolute; left: 22px; top: 861px; color: var(--white); font-size: 14px; }
  .brand-name {
    position: absolute; right: 24px; top: 852px; color: var(--white);
    font-size: 32px; font-weight: 400; letter-spacing: -0.5px;
  }
</style>
</head>
<body>
<main class="slide">
  <div class="header-band"></div>
  <div class="header-shade"></div>
  <h1 class="slide-title">Sample Slide For Free</h1>

  <svg class="download-icon" viewBox="0 0 92 92" aria-hidden="true">
    <circle cx="46" cy="46" r="42" fill="none" stroke="#2bb5c2" stroke-width="5"/>
    <line x1="46" y1="22" x2="46" y2="66" stroke="#2bb5c2" stroke-width="5" stroke-linecap="round"/>
    <polyline points="30,52 46,68 62,52" fill="none" stroke="#2bb5c2" stroke-width="5" stroke-linecap="round" stroke-linejoin="round"/>
  </svg>

  <p class="metric-label">City Data</p>
  <p class="metric-value">$22 Million USD</p>
  <div class="thin-rule"></div>
  <p class="location-note">Colombia, and an historic neighborhood</p>
  <div class="gold-rule"></div>

  <section class="targets-box" aria-label="Annual mapping targets"></section>
  <svg class="divider-slash" viewBox="0 0 140 210" aria-hidden="true">
    <line x1="131" y1="8" x2="10" y2="200" stroke="#f5c018" stroke-width="5"/>
  </svg>

  <div class="target target--left">
    <div class="target-figure">20<sup>%</sup></div>
    <div class="target-name">Mapping</div>
    <div class="target-caption">Per Annum Target</div>
  </div>
  <div class="target target--right">
    <div class="target-figure">10<sup>%</sup></div>
    <div class="target-name">Mapping</div>
    <div class="target-caption">Per Annum Target</div>
  </div>

  <div class="footer-shade"></div>
  <footer class="footer-band"></footer>
  <span class="page-number">3</span>
  <span class="brand-name">civicgrid</span>
</main>
</body>
</html>
```